Business Card Design Project

I need a business card designed that is clean, simple and elegant.
I am a fashion and advertising photographer based in Cape Town and Durban South Africa.
check out my website: www.brennowalsh.co.za for ideas
Updates
Hi all,
Thanks for your submissions so far!
Please note:
I want no more than than black, white and/or grey to be used.
I don't want any photos used.
I would like the card to be double sided.
I would like to continue the design similar to the past ones Ive used.
I hope this helps, please send me further questions should you have any.
many thanks!
Brenno
Hi,
Please have a look at the jpg I loaded(called inspiration) which is the direction or inspiration I am aiming at.
Also PLEASE remember NO PHOTOS to be included on the card
many thanks!!
Target Market(s)
You can look at my site to get a better understanding of the audience:
www.brennowalsh.co.za
Industry/Entity Type
Advertising
Requirements
Must have
- Clean design which can also be used for a watermark on photographs
perhaps black background with white text/grey
company called: Brenno Walsh Photography
Nice to have
- below I have added logos that I have used in the past.
Should not have
- pictures of cameras
tacky elements

```html
<!DOCTYPE html>
<html lang="en">
<head>
<meta charset="utf-8">
<title>Brenno Walsh Photography – Business Card Options</title>
<link rel="stylesheet" href="https://fonts.googleapis.com/css2?family=Montserrat:wght@500&family=Arimo:wght@400&family=Courier+Prime:wght@700&display=swap">
<style>
  :root {
    --page: #ffffff;
    --label: #9a9a9a;
    --card-black: #000000;
    --card-ink: #0b0c0e;
    --film-grey: #4a4a4a;
    --slate: #333333;
    --slate-circle: #424242;
    --bracket: #5a5a5a;
    --mark-grey: #6e6e6e;
    --name-light: #d9d9d9;
    --name-mid: #8c8c8c;
    --white: #ffffff;
    --hole: #ffffff;
  }
  * { margin: 0; padding: 0; box-sizing: border-box; }
  html, body { width: 1088px; height: 1200px; overflow: hidden; background: var(--page); }
  .board {
    position: absolute; left: 10px; top: 0;
    width: 960px; height: 1080px;
    transform: scale(1.1111); transform-origin: 0 0;
  }
  .option-label {
    position: absolute; transform: translateX(-50%);
    font-family: "Courier Prime", monospace; font-weight: 700;
    font-size: 40px; color: var(--label); line-height: 1;
  }
  .card { position: absolute; overflow: hidden; }
  .card--rounded { border-radius: 16px; background: var(--card-black); }
  .card--ink { background: var(--card-ink); }
  .card--film { background: var(--film-grey); }
  .card--slate { background: var(--slate); }

  .wordmark {
    position: absolute; font-family: "Montserrat", sans-serif; font-weight: 500;
    text-transform: uppercase; line-height: 1; letter-spacing: 0.6px; white-space: nowrap;
  }
  .wordmark .line { display: block; }
  .centered { transform: translateX(-50%); text-align: center; }

  .mark-dot { position: absolute; border-radius: 50%; background: var(--mark-grey); }
  .mark-lockup {
    position: absolute; display: flex; align-items: center; gap: 10px;
    transform: translate(-50%, -50%);
    font-family: "Montserrat", sans-serif; font-weight: 500; letter-spacing: 0.6px;
    color: var(--name-mid); white-space: nowrap;
  }
  .mark-lockup .mark-dot { position: static; }

  .bracket { position: absolute; width: 40px; height: 40px; border: 0 solid var(--bracket); }
  .bracket.tl { border-top-width: 4px; border-left-width: 4px; }
  .bracket.tr { border-top-width: 4px; border-right-width: 4px; }
  .bracket.bl { border-bottom-width: 4px; border-left-width: 4px; }
  .bracket.br { border-bottom-width: 4px; border-right-width: 4px; }

  .contact {
    position: absolute; font-family: "Arimo", sans-serif; color: var(--white);
  }
  .contact p { font-size: 9.5px; line-height: 16.5px; }
  .contact .web { font-size: 14.5px; line-height: 18px; margin-top: 1px; }

  .film-hole { position: absolute; width: 13px; height: 10px; border-radius: 2px; background: var(--hole); }
</style>
</head>
<body>
<main class="board">

  <!-- Option A -->
  <span class="option-label" style="left:248px; top:12px;">a</span>
  <section class="card card--rounded" style="left:72px; top:64px; width:356px; height:202px;">
    <div class="mark-lockup" style="left:178px; top:98px; font-size:17px;">
      <span class="mark-dot" style="width:36px; height:36px;"></span>
      <span>BRENNOWALSH</span>
    </div>
  </section>
  <section class="card card--rounded" style="left:72px; top:295px; width:356px; height:202px;">
    <span class="bracket tl" style="left:26px; top:23px;"></span>
    <span class="bracket tr" style="right:26px; top:23px;"></span>
    <span class="bracket bl" style="left:26px; bottom:23px;"></span>
    <span class="bracket br" style="right:26px; bottom:23px;"></span>
    <div class="wordmark centered" style="left:178px; top:40px; font-size:19px;">
      <span class="line" style="color:var(--name-light);">BRENNOWALSH</span>
      <span class="line" style="color:var(--name-mid);">PHOTOGRAPHY</span>
    </div>
    <div class="contact" style="left:41px; top:102px;">
      <p>+27 (0)82 555 0142</p>
      <p>+27 (0)31 555 0187</p>
      <p>brenno@brennowalsh.co.za</p>
      <p class="web">www.brennowalsh.co.za</p>
    </div>
  </section>

  <!-- Option B -->
  <span class="option-label" style="left:714px; top:12px;">b</span>
  <section class="card card--rounded" style="left:537px; top:64px; width:355px; height:202px;">
    <span class="mark-dot" style="left:139px; top:49px; width:76px; height:76px;"></span>
    <div class="wordmark centered" style="left:177px; top:138px; font-size:19px;">
      <span class="line" style="color:var(--name-light);">BRENNOWALSH</span>
      <span class="line" style="color:var(--name-mid);">PHOTOGRAPHY</span>
    </div>
  </section>
  <section class="card card--rounded" style="left:537px; top:296px; width:355px; height:202px;">
    <span class="bracket tl" style="left:26px; top:23px;"></span>
    <span class="bracket tr" style="right:26px; top:23px;"></span>
    <span class="bracket bl" style="left:26px; bottom:23px;"></span>
    <span class="bracket br" style="right:26px; bottom:23px;"></span>
    <div class="wordmark centered" style="left:177px; top:44px; font-size:21px; color:var(--white);">BRENNOWALSH</div>
    <div class="contact" style="left:41px; top:101px;">
      <p>+27 (0)82 555 0142</p>
      <p>+27 (0)31 555 0187</p>
      <p>brenno@brennowalsh.co.za</p>
      <p class="web">www.brennowalsh.co.za</p>
    </div>
  </section>

  <!-- Option C -->
  <span class="option-label" style="left:260px; top:548px;">c</span>
  <section class="card card--ink" style="left:123px; top:601px; width:281px; height:159px;">
    <div class="mark-lockup" style="left:140px; top:79px; font-size:15px;">
      <span class="mark-dot" style="width:30px; height:30px;"></span>
      <span>BRENNOWALSH</span>
    </div>
  </section>
  <section class="card card--film" style="left:184px; top:776px; width:160px; height:279px;">
    <span class="film-hole" style="left:6px; top:22px;"></span>
    <span class="film-hole" style="left:6px; top:43px;"></span>
    <span class="film-hole" style="left:6px; top:63px;"></span>
    <span class="film-hole" style="left:6px; top:84px;"></span>
    <span class="film-hole" style="left:6px; top:104px;"></span>
    <span class="film-hole" style="left:6px; top:125px;"></span>
    <span class="film-hole" style="left:6px; top:146px;"></span>
    <span class="film-hole" style="left:6px; top:166px;"></span>
    <span class="film-hole" style="left:6px; top:187px;"></span>
    <span class="film-hole" style="left:6px; top:207px;"></span>
    <span class="film-hole" style="left:6px; top:228px;"></span>
    <span class="film-hole" style="left:6px; top:248px;"></span>
    <span class="film-hole" style="left:142px; top:22px;"></span>
    <span class="film-hole" style="left:142px; top:43px;"></span>
    <span class="film-hole" style="left:142px; top:63px;"></span>
    <span class="film-hole" style="left:142px; top:84px;"></span>
    <span class="film-hole" style="left:142px; top:104px;"></span>
    <span class="film-hole" style="left:142px; top:125px;"></span>
    <span class="film-hole" style="left:142px; top:146px;"></span>
    <span class="film-hole" style="left:142px; top:166px;"></span>
    <span class="film-hole" style="left:142px; top:187px;"></span>
    <span class="film-hole" style="left:142px; top:207px;"></span>
    <span class="film-hole" style="left:142px; top:228px;"></span>
    <span class="film-hole" style="left:142px; top:248px;"></span>
    <div class="wordmark centered" style="left:80px; top:83px; font-size:12.5px;">
      <span class="line" style="color:var(--name-light);">BRENNOWALSH</span>
      <span class="line" style="color:#9a9a9a;">PHOTOGRAPHY</span>
    </div>
    <div class="contact centered" style="left:80px; top:192px;">
      <p style="font-size:7px; line-height:12.5px;">+27 (0)82 555 0142</p>
      <p style="font-size:7px; line-height:12.5px;">+27 (0)31 555 0187</p>
      <p style="font-size:7px; line-height:12.5px;">brenno@brennowalsh.co.za</p>
      <p class="web" style="font-size:10.5px; line-height:13px;">www.brennowalsh.co.za</p>
    </div>
  </section>

  <!-- Option D -->
  <span class="option-label" style="left:700px; top:564px;">d</span>
  <section class="card card--ink" style="left:536px; top:614px; width:356px; height:202px;">
    <span class="mark-dot" style="left:50px; top:63px; width:78px; height:78px;"></span>
    <div class="wordmark" style="left:142px; top:89px; font-size:19px;">
      <span class="line" style="color:var(--mark-grey);">BRENNOWALSH</span>
      <span class="line" style="color:var(--mark-grey);">PHOTOGRAPHY</span>
    </div>
  </section>
  <section class="card card--slate" style="left:536px; top:845px; width:356px; height:202px;">
    <span class="mark-dot" style="left:0; top:-18px; width:238px; height:238px; background:var(--slate-circle); margin-left:-119px; left:119px;"></span>
    <div class="wordmark" style="right:21px; top:23px; font-size:23px; color:var(--white);">BRENNOWALSH</div>
    <div class="contact" style="left:22px; top:113px;">
      <p>+27 (0)82 555 0142</p>
      <p>+27 (0)31 555 0187</p>
      <p>brenno@brennowalsh.co.za</p>
      <p class="web">www.brennowalsh.co.za</p>
    </div>
  </section>

</main>
</body>
</html>
```